2 Sided 4x6 flyer card for marketing

We are Vapor store and need a nice flyer to hand out for new business
we want 2 sided 4 x 6 flyer
Side 1
MistLoftix
48317 Tamsel Ridge Rd
Garden Grove Ca 90417
714-555-0193
www.mistloftix.com

We have Friendly knowledgable staff with a great atmosphere
enjoy a fresh made smoothie at our Juice bar
In Stock Mechanical Mods
We have Starter Kits
We carry a large assortment of E Juices Like:
Tumbo Nectar
9 Lanterns
Veld
Zenorick
Drift Otter

Side 2
Offer
3 cut out coupons
#1
Any Flavor 10 Ml Tumbo Nectar EJuice with any purchase over $20.00

#2
Free 12oz Fruit Smoothie and $2.50 off any E Juice any Size, brand or flavor with any purchase over $25.00

#3
Buy any 3 10 ml E Juices and get the 4th one FREE of equal or lesser value

Please read brief we have gone a different direction.

Reason: We have changed it to a 4 x 6 flyer 2 sided please read brief

Target Market(s)

We are looking Vapor users and smokers

Industry/Entity Type

Marketing

Font styles to use
Sans Serif

Requirements
Must have
• Graphic design skills

```html
<!DOCTYPE html>
<html lang="en">
<head>
<meta charset="utf-8">
<title>MistLoftix Flyer Card</title>
<link rel="stylesheet" href="https://fonts.googleapis.com/css2?family=Didact+Gothic&family=Poiret+One&display=swap">
<style>
  :root {
    --blue: #0a72b8;
    --blue-deep: #075a99;
    --green: #a6ce39;
    --white: #ffffff;
    --label: #9a9a9a;
    --thin: "Poiret One", sans-serif;
    --sans: "Didact Gothic", sans-serif;
  }
  * { margin: 0; padding: 0; box-sizing: border-box; }
  html, body { width: 848px; height: 1200px; overflow: hidden; background: var(--white); }
  body { position: relative; font-family: var(--sans); }

  .side-label {
    position: absolute; left: 66px;
    font-family: var(--sans); font-size: 32px; letter-spacing: 1px;
    color: var(--label);
  }
  .side-label--front { top: 58px; }
  .side-label--back { top: 608px; }

  .card {
    position: absolute; left: 67px; width: 684px; height: 456px;
    overflow: hidden;
    box-shadow: 0 6px 14px rgba(0,0,0,.22);
  }
  .card--front { top: 114px; background: var(--green); }
  .card--back { top: 659px; display: flex; }

  /* front */
  .intro {
    position: absolute; left: 0; top: 0; width: 684px; height: 257px;
    background: linear-gradient(180deg, var(--blue-deep) 0%, var(--blue) 45%);
    border-radius: 0 0 24px 24px;
    box-shadow: 0 5px 8px rgba(0,0,0,.2);
  }
  .intro__text {
    position: absolute; left: 31px; top: 120px; width: 640px;
    font-family: var(--thin); font-size: 37px; line-height: 44px;
    color: var(--white); letter-spacing: -0.5px;
  }
  .brand-tab {
    position: absolute; left: 92px; top: 0; width: 509px; height: 108px;
    background: linear-gradient(180deg, #ffffff 70%, #ececec 100%);
    border-radius: 0 0 20px 20px;
    box-shadow: 0 4px 8px rgba(0,0,0,.3);
    display: flex; align-items: center; justify-content: center; gap: 16px;
  }
  .brand-tab__mark { width: 36px; height: 36px; background: var(--green); }
  .brand-tab__name { font-family: var(--sans); font-size: 58px; color: var(--blue); }

  .stock-tab {
    position: absolute; left: 35px; top: 257px; width: 468px; height: 69px;
    background: var(--green); border-radius: 0 0 20px 20px;
    box-shadow: 0 4px 8px rgba(0,0,0,.2);
    padding: 16px 0 0 18px;
    font-size: 24px; color: var(--white); z-index: 2;
  }
  .juice-box {
    position: absolute; left: 35px; top: 310px; width: 468px; height: 92px;
    background: var(--blue); border-radius: 0 0 20px 20px;
    box-shadow: 0 4px 8px rgba(0,0,0,.2);
    padding: 30px 0 0 20px;
    font-size: 19px; line-height: 23px; color: var(--white);
  }
  .contact {
    position: absolute; left: 513px; top: 349px; width: 163px; height: 107px;
    background: var(--blue); border-radius: 16px 16px 0 0;
    padding: 24px 0 0 8px;
    font-size: 12.5px; line-height: 14.5px; color: var(--white);
    font-style: normal;
  }

  /* back */
  .coupon {
    position: relative; width: 228px; height: 456px; text-align: center;
    --edge: 20px;
    background:
      repeating-linear-gradient(90deg, var(--dash) 0 24px, transparent 24px 48px) top / 100% var(--edge) no-repeat,
      repeating-linear-gradient(90deg, var(--dash) 0 24px, transparent 24px 48px) bottom / 100% var(--edge) no-repeat,
      repeating-linear-gradient(180deg, var(--dash) 0 24px, transparent 24px 48px) left / var(--edge) 100% no-repeat,
      repeating-linear-gradient(180deg, var(--dash) 0 24px, transparent 24px 48px) right / var(--edge) 100% no-repeat,
      var(--panel);
    color: var(--ink);
  }
  .coupon--green { --panel: var(--green); --dash: var(--white); --ink: var(--white); }
  .coupon--blue { --panel: var(--blue); --dash: var(--green); --ink: var(--green); width: 228px; }
  .coupon--white { --panel: var(--white); --dash: var(--blue); --ink: var(--blue); }
  .coupon > * { position: absolute; left: 0; width: 100%; }
  .coupon__title { top: 22px; font-family: var(--thin); font-size: 38px; }
  .coupon__offer { top: 96px; font-family: var(--thin); font-size: 37px; font-weight: 400; letter-spacing: -0.5px; }
  .coupon__detail { font-family: var(--thin); font-size: 14.5px; line-height: 21px; }
  .coupon__note { font-family: var(--thin); font-size: 22px; line-height: 23px; }
  .coupon__price { font-family: var(--thin); font-size: 41px; }
  .coupon__big { font-family: var(--thin); font-size: 27px; }
  .coupon__free { top: 247px; font-family: var(--thin); font-size: 44px; }
  .coupon__brand { top: 372px; font-family: var(--sans); font-size: 22px; }
  .coupon--green .coupon__title { color: var(--white); }
</style>
</head>
<body>
  <div class="side-label side-label--front">front</div>

  <section class="card card--front">
    <div class="intro">
      <p class="intro__text">we have friendly knowledgable staff with a great atmosphere. enjoy a fresh made smoothie at our juice bar.</p>
    </div>
    <div class="brand-tab">
      <span class="brand-tab__mark"></span>
      <span class="brand-tab__name">MistLoftix</span>
    </div>
    <div class="juice-box">We carry a large assortment of E Juices Like:<br>Tumbo Nectar, 9 Lanterns, Veld, Zenorick &amp; Drift Otter</div>
    <div class="stock-tab">In Stock: Mechanical Mods, Starter Kits</div>
    <address class="contact">MistLoftix<br>48317 Tamsel Ridge Rd<br>Garden Grove Ca 90417<br>714-555-0193<br>www.mistloftix.com</address>
  </section>

  <div class="side-label side-label--back">back</div>

  <section class="card card--back">
    <article class="coupon coupon--green">
      <h2 class="coupon__title">COUPON</h2>
      <h3 class="coupon__offer">Any Flavor</h3>
      <p class="coupon__detail" style="top:157px">10 Ml Tumbo Nectar EJuice</p>
      <p class="coupon__note" style="top:224px">with any<br>purchase over</p>
      <p class="coupon__price" style="top:284px">$20.00</p>
      <p class="coupon__brand">MistLoftix</p>
    </article>

    <article class="coupon coupon--blue">
      <h2 class="coupon__title">COUPON</h2>
      <h3 class="coupon__offer">Free</h3>
      <p class="coupon__detail" style="top:157px">12oz Fruit Smoothie</p>
      <p class="coupon__detail" style="top:186px">and <span class="coupon__big">$2.50</span> off</p>
      <p class="coupon__detail" style="top:218px">any E Juice any Size,<br>brand or flavor</p>
      <p class="coupon__detail" style="top:278px">with any purchase over</p>
      <p class="coupon__price" style="top:298px">$25.00</p>
      <p class="coupon__brand">MistLoftix</p>
    </article>

    <article class="coupon coupon--white">
      <h2 class="coupon__title">COUPON</h2>
      <h3 class="coupon__offer">Buy any 3</h3>
      <p class="coupon__detail" style="top:157px">10 ml E Juices</p>
      <p class="coupon__detail" style="top:208px">and get the <span class="coupon__big">4th</span> one</p>
      <p class="coupon__free">FREE</p>
      <p class="coupon__detail" style="top:297px">of equal or lesser value</p>
      <p class="coupon__brand">MistLoftix</p>
    </article>
  </section>
</body>
</html>
```